Business Card Design Project

The logo I included in my order was a previous image that we've used for shirts, signs, magnets, etc. We've decided to go back to that logo, with some updates.
We need to add "Inc." after "Brindel Roofing,"
Also, I need the logo with a transparent background so that I can use it on other projects.

The business cards will be the first item I order with the new logo. The employee's info is:
Derek Pallow
Sales Manager
484-611-3907
dpallow@brindelroofinginc.example

Also, I want a "Find us on Linkora" icon on the card, along with our web address, www.brindelroofinginc.example.

Any questions, please email or call me:
norabrindel@mailbox.example
484-290-6153

Reason: This is the first time I've tried Pixel Forum.

My timetable changed and I need to select a design by the end of the work day, 6 hours from now.Thanks so much for all of the super designs.

Target Market(s)

Homeowners

Industry/Entity Type

Business

Font styles to use
Serif

Requirements
Must have
• Transparent background
Similar to logo in photo I sent you

```html
<!DOCTYPE html>
<html lang="en">
<head>
<meta charset="utf-8">
<title>Brindel Roofing Inc. – Business Card</title>
<link rel="stylesheet" href="https://fonts.googleapis.com/css2?family=Cormorant+Garamond:wght@500&family=Questrial&display=swap">
<style>
  :root {
    --card-base: #e6e1e1;
    --card-panel: #d6d6d7;
    --ink: #111111;
    --brand-blue: #34458a;
    --serif: "Cormorant Garamond", Georgia, serif;
    --sans: "Questrial", "Helvetica Neue", Arial, sans-serif;
  }
  html, body {
    margin: 0;
    padding: 0;
    width: 1200px;
    height: 686px;
    overflow: hidden;
    background: #ffffff;
  }
  .card {
    position: relative;
    width: 1200px;
    height: 686px;
    background: var(--card-base);
    overflow: hidden;
    color: var(--ink);
  }
  .card__panel {
    position: absolute;
    inset: 0;
  }
  .brand {
    position: absolute;
    left: 40px;
    top: 70px;
    width: 340px;
    text-align: center;
  }
  .brand__name {
    display: flex;
    align-items: center;
    justify-content: center;
    gap: 14px;
    font-family: var(--sans);
    font-size: 40px;
    line-height: 1.1;
    letter-spacing: 1px;
  }
  .brand__mark {
    width: 26px;
    height: 26px;
    background: var(--ink);
    flex: none;
  }
  .brand__phone {
    margin-top: 70px;
    font-family: var(--sans);
    font-size: 34px;
    letter-spacing: 1px;
  }
  .contact {
    position: absolute;
    left: 0;
    top: 296px;
    width: 566px;
    text-align: center;
  }
  .contact__name {
    font-family: var(--serif);
    font-weight: 500;
    font-size: 84px;
    line-height: 1;
    letter-spacing: 3px;
    text-shadow: 2px 3px 4px rgba(0,0,0,0.25);
  }
  .contact__title {
    margin-top: 8px;
    font-family: var(--sans);
    font-size: 40px;
    letter-spacing: 2px;
  }
  .contact__phone {
    margin-top: 14px;
    font-family: var(--sans);
    font-size: 42px;
    letter-spacing: 2px;
  }
  .contact__email {
    margin-top: 12px;
    font-family: var(--sans);
    font-size: 28px;
    letter-spacing: 1px;
  }
  .social {
    position: absolute;
    left: 800px;
    top: 300px;
    width: 330px;
    display: flex;
    align-items: center;
    justify-content: center;
    gap: 12px;
    font-family: var(--sans);
    font-size: 38px;
    color: var(--brand-blue);
  }
  .social__mark {
    width: 24px;
    height: 24px;
    background: var(--brand-blue);
    flex: none;
  }
  .website {
    position: absolute;
    left: 680px;
    top: 460px;
    width: 520px;
    text-align: center;
    font-family: var(--sans);
    font-size: 31px;
    letter-spacing: 1px;
    color: var(--brand-blue);
  }
</style>
</head>
<body>
<div class="card">
  <svg class="card__panel" width="1200" height="686" viewBox="0 0 1200 686" aria-hidden="true">
    <polygon points="1080,0 1200,0 1200,686 450,686" fill="var(--card-panel)"/>
  </svg>

  <div class="brand">
    <div class="brand__name"><span class="brand__mark"></span>Brindel Roofing Inc.</div>
    <div class="brand__phone">610-555-0148</div>
  </div>

  <div class="contact">
    <div class="contact__name">Derek Pallow</div>
    <div class="contact__title">Sales Manager</div>
    <div class="contact__phone">484-611-3907</div>
    <div class="contact__email">dpallow@brindelroofinginc.example</div>
  </div>

  <div class="social"><span class="social__mark"></span>Find us on Linkora</div>
  <div class="website">www.brindelroofinginc.example</div>
</div>
</body>
</html>
```